依頼詳細
今ある幸せをメッセージとして書き、ご報告と共にお祈り頂きます。それ以外にも献歌などのサブ的なイベントのご案内を盛り込みたいと思います。
記載項目
詳細は添付資料をご確認願います。また、添付画像をご利用下さい。
サイズ
A4
ページ数
片面
希望イメージ
シンプル 複雑
単色 カラフル
暗い 明るい
日常 高級
遊び心 厳粛
未来的 伝統的
女性的 男性的
希望する色
納品ファイル
• イラストレーター形式 (.ai)
補足説明
アウトラインの有るもの、無いもの双方でお願い致します。添付画像は加工OKです。
■ 選んだ理由

選定にあたりましては弊社内でメイン画像枠の取り方(グラデーション/エッジ)で大きく選考しました。その結果、グラデーションが良いとの意見が過半数を超え、その中で更に投票方式によりhasuventoさんのご提案を選ばせて頂きました。慰霊そしてお客様へのメッセージが重要でありながら、サブイベントでは楽しさを感じさせ、行ってみたくなる。弊社が考えるコンセプトそのものでした。
また、度重なる修正依頼にも応じて頂けました事、本当に助かりました。

■ 提案者全員のお礼・コメント

皆様より本当に多くのご提案を頂きました事、この場をお借りし、御礼申し上げます。今回初めてポルメットへの依頼であり、ご提案頂けるのか不安がありましたが、ご応募頂いた皆様が当社のコンセプトをご理解・ご提案頂きました事また、その表現力、感謝の言葉しかありません。今後もお力を頂く機会があろうかと思いますし、是非、依頼をしたいと思います。その時にまたご提案頂く事が出来れば幸いです。

```html
<!DOCTYPE html>
<html lang="ja">
<head>
<meta charset="utf-8">
<title>キャンドル慰霊祭 開催の御案内</title>
<link href="https://fonts.googleapis.com/css2?family=Noto+Serif+JP:wght@400;600;700&family=Noto+Sans+JP:wght@400;500;700&family=Cormorant+Garamond:wght@500&display=swap" rel="stylesheet">
<style>
:root{
  --night:#120d0a;
  --ember:#3a2416;
  --candle:#d9924a;
  --gold:#f2d891;
  --cream:#fffaf0;
  --ink:#3b2e26;
  --muted:#6e5f53;
  --leaf:#8aa25a;
  --bloom:#e58a7c;
  --rose:#c43a3a;
  --line:#cfc4b8;
  --paper:#ffffff;
}
*{margin:0;padding:0;box-sizing:border-box}
html,body{width:855px;height:1200px;overflow:hidden;background:var(--paper)}
body{font-family:"Noto Sans JP",sans-serif;color:var(--ink)}
.flyer{position:relative;width:855px;height:1200px;overflow:hidden;background:var(--paper)}

.hero{position:absolute;left:0;top:0;width:855px;height:690px;
  background:linear-gradient(180deg,var(--night) 0%,var(--night) 50%,var(--ember) 70%,rgba(255,255,255,0) 100%)}
.candles{position:absolute;left:0;top:0;width:320px;height:560px;
  background:radial-gradient(ellipse at 30% 55%,rgba(217,146,74,.55) 0%,rgba(120,60,25,.35) 40%,rgba(18,13,10,0) 75%)}
.flowers{position:absolute;left:20px;top:340px;width:820px;height:320px;
  background:radial-gradient(ellipse at 55% 45%,rgba(229,138,124,.55) 0%,rgba(138,162,90,.45) 35%,rgba(255,255,255,0) 72%)}

.title{position:absolute;left:0;right:0;top:100px;text-align:center;color:var(--cream);
  font-family:"Noto Serif JP",serif;font-weight:700;font-size:44px;letter-spacing:2px}
.title .mark{display:inline-block;width:22px;height:22px;border-radius:50%;background:var(--gold);vertical-align:middle;margin-right:14px}
.title small{font-size:28px;font-weight:600;margin-left:8px}
.date{position:absolute;left:0;right:0;top:172px;text-align:center;color:var(--gold);
  font-family:"Noto Serif JP",serif;font-weight:600;font-size:32px}
.date b{font-size:52px;font-weight:700}
.lead{position:absolute;left:150px;top:250px;width:660px;color:var(--cream);font-size:11px;line-height:1.7;opacity:.9}

.message-lines{position:absolute;left:250px;top:330px;width:440px;color:var(--cream);
  font-family:"Noto Serif JP",serif;font-size:13px;line-height:1}
.message-lines p{padding:7px 0 6px 20px;border-bottom:1px dashed rgba(255,250,240,.45)}
.message-lines p:nth-child(odd){padding-left:0}

.event{position:absolute}
.event h3{font-family:"Noto Serif JP",serif;font-weight:700;font-size:22px;color:var(--ink);white-space:nowrap}
.event h3 span{font-family:"Noto Sans JP",sans-serif;font-weight:500;font-size:14px;margin-left:8px}
.event p{font-size:11px;line-height:1.6;color:var(--muted)}

.singer{position:absolute;left:160px;top:628px;width:130px;height:96px;border-radius:4px;
  background:linear-gradient(135deg,#efe6da,#c9b9a4)}
.song{left:36px;top:730px;width:300px}
.song p{margin-top:6px}

.molle-art{position:absolute;left:420px;top:630px;width:140px;height:130px;border-radius:50%;
  background:radial-gradient(circle,#ffffff 0%,#eceae6 60%,rgba(255,255,255,0) 75%)}
.molle{left:340px;top:762px;width:270px}
.molle p{margin-top:6px}

.bouquet{position:absolute;left:630px;top:630px;width:160px;height:110px;border-radius:4px;
  background:radial-gradient(circle at 50% 50%,#f3b0a2 0%,#e58a7c 40%,#f4ede4 80%)}
.gift{position:absolute;left:620px;top:752px;width:180px;text-align:center;font-family:"Noto Serif JP",serif;
  font-size:14px;color:var(--ink)}

.msgbox{position:absolute;left:36px;top:860px;width:783px;height:172px;background:#f7f3ee;border:1px solid var(--line)}
.msgbox h2{text-align:center;font-family:"Cormorant Garamond",serif;font-weight:500;font-size:18px;letter-spacing:6px;
  color:var(--muted);margin-top:8px}
.msgbox h2::before,.msgbox h2::after{content:"";display:inline-block;width:280px;height:1px;background:var(--line);vertical-align:middle;margin:0 12px}
.msgbox ul{list-style:none;margin:6px 30px 0}
.msgbox li{height:38px;border-bottom:1px dashed var(--line)}

.note{position:absolute;left:36px;top:1040px;width:783px;text-align:center;color:var(--rose);font-size:11px}

.footer{position:absolute;left:0;top:1066px;width:855px;height:134px;background:#f4efe9;border-top:3px solid var(--candle)}
.brand{position:absolute;left:36px;top:30px;font-family:"Noto Serif JP",serif;font-weight:600;font-size:24px;color:var(--ink)}
.brand i{display:inline-block;width:18px;height:18px;border-radius:50%;background:var(--candle);vertical-align:middle;margin-right:10px}
.office{position:absolute;left:64px;top:70px;font-size:12px;color:var(--muted)}
.contact-tag{position:absolute;left:430px;top:36px;background:var(--candle);color:var(--cream);font-size:12px;padding:4px 10px;border-radius:3px}
.address{position:absolute;left:540px;top:26px;font-size:14px;color:var(--ink)}
.phone{position:absolute;left:540px;top:50px;font-family:"Noto Serif JP",serif;font-weight:700;font-size:30px;color:var(--ember);display:flex;align-items:center;gap:6px}
</style>
</head>
<body>
<main class="flyer">
  <section class="hero">
    <div class="candles" role="img" aria-label="暗闇に灯る多数のキャンドルの写真"></div>
    <div class="flowers" role="img" aria-label="色とりどりの花のアレンジメントの写真"></div>

    <h1 class="title"><span class="mark"></span>キャンドル慰霊祭<small>開催の御案内</small></h1>
    <p class="date">2016年 <b>7</b>月<b>16</b>日(土) <b>14</b>時~<b>18</b>時</p>
    <p class="lead">すべての大切な方々へ感謝の気持ちを込めて、ご家族・ご友人とお誘い合わせの上、皆様お揃いでご参加をお待ちしております。</p>

    <div class="message-lines">
      <p>見守ってくれた母に</p>
      <p>いつも言えなかったありがとうを、今こそ伝えたいと思います</p>
      <p>いつも近くで支えてくれている大切な人へ</p>
      <p>あの頃の日々が、今日の私をつくっています</p>
      <p>家族みんなで元気に暮らしています</p>
      <p>これからも見守っていてください</p>
      <p>お届けいたしますね</p>
    </div>
  </section>

  <div class="singer" role="img" aria-label="ギターを手に歌う女性歌手の写真"></div>
  <div class="event song">
    <h3>献 歌<span>14:30 ~ 16:00</span></h3>
    <p>高瀬 美織さん<br>やさしい歌声で会場を包みます。<br>心に残る名曲をお届けいたします。</p>
  </div>

  <div class="molle-art" role="img" aria-label="モールで作った白い動物の作品の写真"></div>
  <div class="event molle">
    <h3>モールアート<span>16:30~</span></h3>
    <p>モールを使って、かわいい作品をつくりましょう。<br>お子様も楽しめます。</p>
  </div>

  <div class="bouquet" role="img" aria-label="花束のプレゼントの写真"></div>
  <p class="gift">お花のプレゼントも</p>

  <section class="msgbox">
    <h2>MESSAGE</h2>
    <ul><li></li><li></li><li></li></ul>
  </section>

  <p class="note">※ご記入のうえ、7月15日までに慰霊祭事務局へご提出をお願いいたします。</p>

  <footer class="footer">
    <p class="brand"><i></i>セレモニーホテル ルミエラ</p>
    <p class="office">2016 キャンドル慰霊祭事務局</p>
    <span class="contact-tag">お問い合わせ</span>
    <p class="address">〒900-0000 みなと市桜木町3番21</p>
    <p class="phone">
      <svg width="26" height="26" viewBox="0 0 24 24" aria-hidden="true"><path fill="currentColor" d="M6.6 10.8a15 15 0 0 0 6.6 6.6l2.2-2.2c.3-.3.7-.4 1-.2 1.1.4 2.3.6 3.6.6.6 0 1 .4 1 1V20c0 .6-.4 1-1 1A17 17 0 0 1 3 4c0-.6.4-1 1-1h3.5c.6 0 1 .4 1 1 0 1.3.2 2.5.6 3.6.1.3 0 .7-.2 1z"/></svg>
      000-123-4567
    </p>
  </footer>
</main>
</body>
</html>
```